Vanta Roving Car Wash and Detail Services, 'needs a logo and card design'

I need a logo and Card design for a new company based in Perth Western Australia called, 'Vanta Roving Car Wash and Detail Services'. I want to offer a mobile car wash and detail service across all the Perth metropolitan areas at lower prices, and offer more reliability. I would like to see designs with colours such as red, white, and black. The final design should communicate trust reliability and confidence in the services I can provide. The card must include my first name 'Ormand' and my mobile number '0417208364' for an obligation free quote.

Target Market(s)

Aimed at anyone who owns and drives a motor vehicle.

Industry/Entity Type

It Company

Contact Information for Business Card

Business Name'Vanta Roving Car Wash and Detail Services', My first name 'Ormand', and my mobile phone '0417208364' for an obligation free quote.

Font styles to use
Serif
Decorative
Script

Colors
ffffff
000000
d3d3d3
ec1f27
7f7f7f

Requirements
Must have
• Business Name'Vanta Roving Car Wash and Detail Services', My first name 'Ormand', and my mobile phone '0417208364' for an obligation free quote.
• Logo design
Nice to have
• A slogan, such as 'I come to you, and wash your car wherever you are' to let customers know I am at their service.
• Car design 'shine and clean feeling'

```html
<!DOCTYPE html>
<html lang="en">
<head>
<meta charset="utf-8">
<title>Vanta Roving Car Wash and Detail Services – Business Card</title>
<link rel="stylesheet" href="https://fonts.googleapis.com/css2?family=Lato:wght@300;400;900&display=swap">
<style>
  :root {
    --red: #ec1f27;
    --black: #000000;
    --charcoal: #2a2a2c;
    --charcoal-deep: #1b1b1d;
    --white: #ffffff;
    --light-grey: #d3d3d3;
    --mid-grey: #7f7f7f;
    --backdrop: #d9d6d1;
  }
  * { box-sizing: border-box; margin: 0; padding: 0; }
  html, body {
    width: 1200px;
    height: 780px;
    overflow: hidden;
    background: var(--backdrop);
    font-family: "Lato", Arial, sans-serif;
  }
  .canvas {
    width: 1200px;
    height: 780px;
    display: flex;
    align-items: center;
    justify-content: center;
    gap: 40px;
  }
  .card {
    position: relative;
    width: 540px;
    height: 310px;
    border-radius: 18px;
    overflow: hidden;
    box-shadow: 0 10px 28px rgba(0,0,0,0.22);
  }

  /* Front: white face with brand name */
  .card-front {
    background: linear-gradient(160deg, var(--white) 0%, #f1f1f1 60%, #e4e4e4 100%);
  }
  .front-swoosh {
    position: absolute;
    inset: 0;
    width: 100%;
    height: 100%;
  }
  .brand {
    position: absolute;
    top: 78px;
    right: 52px;
    width: 300px;
    text-align: center;
    color: var(--red);
    font-weight: 900;
    text-transform: uppercase;
  }
  .brand-name {
    font-size: 38px;
    line-height: 1;
    letter-spacing: 1px;
  }
  .brand-tagline {
    margin-top: 8px;
    font-size: 12.5px;
    letter-spacing: 1.2px;
  }

  /* Back: dark contact face */
  .card-back {
    background: radial-gradient(ellipse at 70% 20%, #3a3a3d 0%, var(--charcoal) 45%, var(--charcoal-deep) 100%);
    color: var(--white);
  }
  .back-tab {
    position: absolute;
    left: -30px;
    top: 44px;
    width: 60px;
    height: 60px;
    border-radius: 50%;
    background: var(--red);
  }
  .holder-name {
    position: absolute;
    left: 58px;
    top: 54px;
    font-size: 32px;
    font-weight: 900;
    letter-spacing: 2px;
    text-transform: uppercase;
    color: var(--light-grey);
  }
  .contact-list {
    position: absolute;
    left: 58px;
    top: 124px;
    list-style: none;
  }
  .contact-item {
    display: flex;
    align-items: center;
    gap: 12px;
    font-size: 19px;
    font-weight: 400;
    line-height: 30px;
    color: var(--white);
  }
  .contact-icon {
    width: 22px;
    height: 22px;
    flex: none;
  }
  .slogan {
    position: absolute;
    left: 58px;
    top: 200px;
    font-size: 19px;
    font-weight: 300;
    line-height: 26px;
    color: var(--light-grey);
  }
</style>
</head>
<body>
<main class="canvas">

  <section class="card card-front" aria-label="Card front">
    <svg class="front-swoosh" viewBox="0 0 540 310" aria-hidden="true">
      <path d="M0 168 C 150 262 340 300 540 306 L540 310 L0 310 Z" fill="#262628"/>
      <path d="M0 156 C 150 250 340 290 540 298" fill="none" stroke="#ec1f27" stroke-width="3"/>
    </svg>
    <div class="brand">
      <p class="brand-name">Vanta Roving</p>
      <p class="brand-tagline">Car Wash and Detail Services</p>
    </div>
  </section>

  <section class="card card-back" aria-label="Card back">
    <span class="back-tab" aria-hidden="true"></span>
    <h1 class="holder-name">Ormand</h1>
    <ul class="contact-list">
      <li class="contact-item">
        <svg class="contact-icon" viewBox="0 0 22 22" aria-hidden="true">
          <rect width="22" height="22" rx="3" fill="#ec1f27"/>
          <path d="M7 5 L9.5 5 L10.5 8 L9 9.2 Q10.3 12 12.8 13 L14 11.5 L17 12.5 L17 15 Q16.5 17 14.5 17 Q6 16 5 7.5 Q5 5.5 7 5 Z" fill="#ffffff"/>
        </svg>
        <span>0417208364</span>
      </li>
      <li class="contact-item">
        <svg class="contact-icon" viewBox="0 0 22 22" aria-hidden="true">
          <rect width="22" height="22" rx="3" fill="#ec1f27"/>
          <rect x="5" y="7" width="12" height="9" fill="none" stroke="#ffffff" stroke-width="1.6"/>
          <path d="M5 7 L11 12 L17 7" fill="none" stroke="#ffffff" stroke-width="1.6"/>
        </svg>
        <span>hello@vantaroving.au</span>
      </li>
    </ul>
    <p class="slogan">I come to you<br>and wash your car<br>wherever you are</p>
  </section>

</main>
</body>
</html>
```